Snapframe Party Rentals New Business Card*

Need a business card designed for a Photo Booth Hire company.Must look very professional and colorful.A new creative logo would be a bonus. Our current logo is attached on here.

Contact Information for Business Card

Business Name: SNAPFRAME PARTY RENTALS
Contact Person: MARCUS OKAFOR
Mobile: 0491862035
Email: INFO@SNAPFRAMEPARTY.EXAMPLE
Website: WWW.SNAPFRAMEPARTY.EXAMPLE
Facebook: WWW.SOCIALNET.EXAMPLE/SNAPFRAME.PARTY.RENT

Font styles to use
Serif
Sans Serif
Script

Colors

Designer to choose colors to be used in the design.

Requirements
Must have
• Bonus if the colors match our website.

```html
<!DOCTYPE html>
<html lang="en">
<head>
<meta charset="utf-8">
<title>Snapframe Party Rentals – Business Card</title>
<link href="https://fonts.googleapis.com/css2?family=Oswald:wght@500;600&family=Montserrat:wght@300;400;700&display=swap" rel="stylesheet">
<style>
  :root {
    --navy: #0f3d5c;
    --navy-line: #5b6f7c;
    --orange: #f0702a;
    --charcoal: #2e2e2e;
    --mist: #e6e6e6;
    --ink: #4a4a4a;
    --paper: #ffffff;
    --backdrop: #d9dadc;
  }
  * { box-sizing: border-box; margin: 0; padding: 0; }
  html, body { width: 1200px; height: 900px; overflow: hidden; }
  body {
    background: var(--backdrop);
    position: relative;
    font-family: "Montserrat", sans-serif;
  }
  .card {
    position: absolute;
    left: 250px;
    width: 700px;
    height: 400px;
    overflow: hidden;
    box-shadow: 0 6px 18px rgba(0,0,0,0.18);
  }
  .card--front { top: 30px; background: var(--paper); }
  .card--back { top: 470px; background: var(--navy); }

  /* Wordmark */
  .wordmark {
    display: flex;
    align-items: center;
    gap: 14px;
  }
  .wordmark__square {
    width: 22px; height: 22px;
    border: 3px solid currentColor;
    flex: none;
  }
  .wordmark__name {
    font-family: "Oswald", sans-serif;
    font-weight: 600;
    letter-spacing: 2px;
    text-transform: uppercase;
    line-height: 1;
  }
  .tagline {
    font-family: "Montserrat", sans-serif;
    font-weight: 400;
    font-size: 8px;
    letter-spacing: 0.6px;
    text-transform: uppercase;
  }

  /* Front */
  .front__brand {
    position: absolute; left: 46px; top: 44px;
    color: var(--navy);
  }
  .front__brand .wordmark__name { font-size: 30px; }
  .front__brand .tagline { color: var(--ink); margin-top: 8px; margin-left: 36px; }
  .front__person {
    position: absolute; left: 46px; top: 150px; width: 300px;
    font-family: "Oswald", sans-serif; font-weight: 500;
    font-size: 26px; letter-spacing: 3px; color: var(--navy);
    padding-bottom: 10px;
    border-bottom: 2px solid var(--navy);
  }
  .contact-list {
    position: absolute; left: 46px; top: 218px;
    list-style: none;
  }
  .contact-list li {
    display: flex; align-items: center; gap: 10px;
    font-size: 14px; font-weight: 300; color: var(--ink);
    margin-bottom: 11px;
  }
  .contact-list svg { width: 14px; height: 14px; flex: none; fill: var(--orange); }
  .contact-list .accent { color: var(--orange); font-weight: 700; }
  .front__art {
    position: absolute; right: 0; top: 0;
    width: 290px; height: 400px;
  }

  /* Back */
  .back__frame-h {
    position: absolute; left: 0; right: 0; top: 70px; height: 260px;
    border-top: 1px solid var(--navy-line);
    border-bottom: 1px solid var(--navy-line);
  }
  .back__frame-v {
    position: absolute; top: 0; bottom: 0; left: 140px; width: 420px;
    border-left: 1px solid var(--navy-line);
    border-right: 1px solid var(--navy-line);
  }
  .back__brand {
    position: absolute; left: 0; right: 0; top: 160px;
    display: flex; flex-direction: column; align-items: center;
    color: var(--paper);
  }
  .back__brand .wordmark__name { font-size: 36px; }
  .back__brand .tagline { color: var(--paper); margin-top: 12px; }
</style>
</head>
<body>

<section class="card card--front" aria-label="Business card front">
  <div class="front__brand">
    <div class="wordmark">
      <span class="wordmark__square"></span>
      <span class="wordmark__name">Snapframe Party Rentals</span>
    </div>
    <p class="tagline">Your city's friendliest photo booth rental company</p>
  </div>

  <h1 class="front__person">MARCUS OKAFOR</h1>

  <ul class="contact-list">
    <li>
      <svg viewBox="0 0 24 24" aria-hidden="true"><path d="M6.6 10.8a15.1 15.1 0 0 0 6.6 6.6l2.2-2.2a1 1 0 0 1 1-.25 11.4 11.4 0 0 0 3.6.57 1 1 0 0 1 1 1V20a1 1 0 0 1-1 1A17 17 0 0 1 3 4a1 1 0 0 1 1-1h3.5a1 1 0 0 1 1 1c0 1.25.2 2.45.57 3.57a1 1 0 0 1-.25 1z"/></svg>
      0491 862 035
    </li>
    <li>
      <svg viewBox="0 0 24 24" aria-hidden="true"><path d="M2 5h20v14H2z M4 7v.5l8 5 8-5V7l-8 5z" fill-rule="evenodd"/></svg>
      info@snapframeparty.example
    </li>
    <li>
      <svg viewBox="0 0 24 24" aria-hidden="true"><path d="M12 2a10 10 0 1 0 0 20 10 10 0 0 0 0-20zm0 2c.9 0 2.1 1.8 2.6 5H9.4C9.9 5.8 11.1 4 12 4zM4.3 11h3a19 19 0 0 0 .2 2h-3.2a8 8 0 0 1 0-2zm5.1 0h5.2a17 17 0 0 1 0 2H9.4a17 17 0 0 1 0-2zm7.3 0h3a8 8 0 0 1 0 2h-3.2a19 19 0 0 0 .2-2zM12 20c-.9 0-2.1-1.8-2.6-5h5.2c-.5 3.2-1.7 5-2.6 5z"/></svg>
      www.<span class="accent">snapframeparty</span>.example
    </li>
    <li>
      <svg viewBox="0 0 24 24" aria-hidden="true"><circle cx="12" cy="12" r="10"/></svg>
      www.socialnet.example/snapframe.party.rent
    </li>
  </ul>

  <svg class="front__art" viewBox="0 0 290 400" role="img" aria-label="Decorative moustache and round glasses illustration in grey, charcoal and orange">
    <defs>
      <linearGradient id="art-tone" x1="0" y1="0" x2="1" y2="1">
        <stop offset="0" stop-color="#e6e6e6"/>
        <stop offset="0.55" stop-color="#bdbdbd"/>
        <stop offset="1" stop-color="#f0702a"/>
      </linearGradient>
    </defs>
    <path d="M290 0 V400 H40 C60 330 120 300 150 240 C180 180 130 120 180 60 C210 25 250 10 290 0 Z" fill="url(#art-tone)"/>
  </svg>
</section>

<section class="card card--back" aria-label="Business card back">
  <div class="back__frame-h"></div>
  <div class="back__frame-v"></div>
  <div class="back__brand">
    <div class="wordmark">
      <span class="wordmark__square"></span>
      <span class="wordmark__name">Snapframe Party Rentals</span>
    </div>
    <p class="tagline">Your city's friendliest photo booth rental company</p>
  </div>
</section>

</body>
</html>
```